We are working with a new commercial flooring contractor in California. They work on schools, hospitals, and government projects.
A few websites for inspiration:
https://plainrockcoverings.com (These guys are competitors and provide the same work our client does).
https://tjtilework.com (Although NOT a contractor, the simplicity of this site is stunning).
https://www.quietlantern.com (NOT a flooring contractor, but this site is modern, and has a boldness to it).
https://www.sagemeadowatelier.com/en-us (website for an Architectural office that is clean and showcases their work. I can see this working for a flooring contractor).
Thank you for taking the time to consider designing a website for us. We are web developers based in Stockton, CA, USA. Most of our projects go through the same process. Understanding this process may help you win a project with us. We custom-code all of our websites in-house. We don’t have any requirements as to what tools you use for your design, but we ask that you follow these guidelines.
IMAGES:
If you use any images or icons in the design, we ask that you have a link to the asset so we can purchase the image/icon. Most of the designs we submit do not have the customer’s images on them unless they have some great images. Be creative; show us the feeling you are trying to portray with your image choices. Use any royalty-free site you choose. We subscribe to Kestral and mainly use their images, but we can purchase images outside of Kestral.
FONTS:
We ask that you identify the fonts you’re using in the design. This can be done in a message if you want. We typically use Vantor Fonts and Kestral Fonts.
CONTENT:
We're always open to different content and ideas. We often submit designs with stock images so the client can see our vision. We typically take pictures after the website launch to use their images with our vision. Lorem Ipsum is fine for paragraphs, but we ask that you make the Headers with correct English. We want to be able to show the vision and identify the sections of the website.
INSPIRATION:
We typically add a couple of links in the brief of websites we like to help you get started in your design.
REVISIONS:
We do not often ask for revisions of the designs unless we see something in the design that may not appeal to the client. If there are slight changes that we want to make, we do that in the development process.
FEEDBACK:
We rarely give feedback on designs during the design process. We are working on many website projects and do not have the time to provide feedback. We usually respond if your request is well thought out and asks specific questions, but a note asking “feedback, please” usually goes unanswered.

```html
<!DOCTYPE html>
<html lang="en">
<head>
<meta charset="utf-8">
<title>Norvale Flooring — Flooring Solutions</title>
<link href="https://fonts.googleapis.com/css2?family=Oswald:wght@500;600&family=Montserrat:wght@400;500;600&display=swap" rel="stylesheet">
<style>
:root{
  --red:#e1262c;
  --ink:#333;
  --dark:#3c3c3c;
  --mint:#e5f0e5;
  --white:#fff;
  --footer:#58595a;
  --footer-deep:#3d3e3f;
  --line:#d6d6d6;
}
*{margin:0;padding:0;box-sizing:border-box}
html,body{width:1200px;height:5124px;overflow:hidden}
body{font-family:"Montserrat",sans-serif;color:var(--ink);background:var(--white);position:relative}
section,header,footer{position:absolute;left:0;width:1200px}
.abs{position:absolute}
.photo{position:absolute}
.heading{font-family:"Oswald",sans-serif;font-weight:500;color:var(--red);text-transform:uppercase;letter-spacing:.5px}
.btn{position:absolute;display:flex;align-items:center;justify-content:center;font-size:10px;font-weight:500;letter-spacing:.5px;text-transform:uppercase;color:var(--white)}
.btn-dark{background:var(--dark)}
.btn-red{background:var(--red)}
p{font-size:12px;line-height:19px}

/* hero */
.hero{top:0;height:590px}
.hero-photo{inset:0;background:
  radial-gradient(ellipse 420px 260px at 78% 38%,rgba(226,222,214,.55),transparent 70%),
  radial-gradient(ellipse 520px 220px at 40% 82%,rgba(176,150,120,.55),transparent 70%),
  linear-gradient(180deg,#4a4845 0%,#6b655e 38%,#8e8172 62%,#6f6254 100%)}
.hero-shade{inset:0;background:linear-gradient(180deg,rgba(0,0,0,.45),rgba(0,0,0,.12) 30%,rgba(0,0,0,.2) 70%,rgba(0,0,0,.35))}
.nav{top:30px;left:22px;display:flex;gap:24px;font-size:12px;font-weight:500;color:var(--white);text-transform:uppercase}
.nav .active{color:var(--red)}
.cta{top:24px;right:22px;width:182px;height:30px;font-size:12px;text-transform:none}
.brand-mark{left:510px;top:6px;width:182px;height:182px;border-radius:50%;background:var(--white);display:flex;align-items:center;justify-content:center;text-align:center}
.brand-name{font-family:"Oswald",sans-serif;font-weight:600;color:var(--red);font-size:30px;line-height:32px;text-transform:uppercase}
.hero-sub{top:284px;width:1200px;text-align:center;color:var(--white);font-size:16px}
.hero-title{top:310px;width:1200px;text-align:center;color:var(--white);font-family:"Oswald",sans-serif;font-weight:500;font-size:42px;line-height:52px;text-transform:uppercase}
.dots{top:548px;left:566px;display:flex;gap:12px}
.dots span{width:15px;height:15px;border-radius:50%;border:2px solid var(--white)}
.dots .on{background:var(--red);border-color:var(--red)}

/* who */
.who{top:590px;height:560px;background:var(--mint)}
.who .photo{left:98px;top:88px;width:492px;height:380px;background:
  radial-gradient(ellipse 180px 150px at 45% 45%,rgba(60,90,170,.55),transparent 70%),
  radial-gradient(ellipse 90px 70px at 30% 78%,rgba(240,170,40,.6),transparent 70%),
  linear-gradient(135deg,#e6e6e3,#cfd0d0 55%,#b9b9b6)}
.who .heading{left:664px;top:156px;font-size:28px}
.who p{left:664px;width:436px;color:#444}

/* where */
.where{top:1150px;height:570px}
.where .photo{inset:0;background:
  radial-gradient(ellipse 260px 200px at 60% 30%,rgba(200,215,190,.6),transparent 70%),
  radial-gradient(ellipse 380px 160px at 35% 88%,rgba(120,100,85,.55),transparent 70%),
  linear-gradient(100deg,#6a5848 0%,#9d8e80 22%,#d9d5ce 52%,#efece7 78%,#d8d5d0 100%)}
.where-box{left:96px;top:130px;width:406px;height:314px;background:rgba(55,55,55,.9)}
.where-box .heading{position:absolute;left:32px;top:50px;font-size:28px}
.where-box p{position:absolute;left:32px;top:108px;width:350px;color:var(--white)}

/* services */
.services{top:1720px;height:640px;background:var(--mint)}
.section-title{position:absolute;top:80px;width:1200px;text-align:center;font-size:30px}
.card{position:absolute;top:154px;width:234px;height:330px}
.card-label{position:absolute;left:20px;bottom:18px;color:var(--white);font-weight:600;font-size:17px;letter-spacing:.5px;text-transform:uppercase}
.card-hover{background:
  radial-gradient(ellipse 120px 80px at 60% 90%,rgba(205,175,135,.6),transparent 70%),
  linear-gradient(180deg,#f7f7f6,#ebe7e1)}
.card-hover .card-label{color:var(--red);bottom:56px}
.next{left:1082px;top:304px;width:36px;height:36px;border-radius:50%;background:var(--dark)}

/* bedroom band */
.band{top:2360px;height:526px;background:
  radial-gradient(ellipse 300px 110px at 36% 74%,rgba(35,33,32,.75),transparent 70%),
  radial-gradient(ellipse 260px 120px at 34% 55%,rgba(140,120,100,.6),transparent 70%),
  radial-gradient(ellipse 120px 150px at 72% 45%,rgba(255,255,255,.6),transparent 70%),
  linear-gradient(90deg,#d8d2c9 0%,#ece9e3 40%,#f4f3f0 70%,#e4dfd8 84%,#b7a898 100%)}

/* work */
.work{top:2886px;height:834px;background:var(--white)}
.work .section-title{top:96px}
.tile{position:absolute;height:263px}
.tile-note{background:linear-gradient(180deg,#f4f4f4,#e8e8e8)}
.tile-note .t{position:absolute;left:26px;top:22px;font-weight:600;font-size:20px;line-height:24px;color:var(--red);text-transform:uppercase}
.tile-note .s{position:absolute;left:26px;top:74px;font-size:11px;color:var(--red);text-transform:uppercase}

/* instagram */
.insta{top:3720px;height:520px;background:var(--mint)}
.insta-box{left:98px;top:56px;width:404px;height:418px;border:2px solid #cdd7cd;text-align:center}
.insta-mark{position:absolute;left:150px;top:52px;width:104px;height:104px;border-radius:50%;background:var(--white);display:flex;align-items:center;justify-content:center}
.insta-mark span{font-family:"Oswald",sans-serif;font-weight:600;font-size:17px;line-height:19px;color:var(--red);text-transform:uppercase}
.insta-text{position:absolute;top:172px;width:400px;font-size:21px;line-height:27px;text-transform:uppercase;color:#222}
.insta-handle{position:absolute;top:320px;width:400px;font-size:16px;text-decoration:underline;color:#222}
.collage{position:absolute;border:3px solid var(--white)}

/* consultation */
.consult{top:4240px;height:460px;background:var(--white)}
.consult .section-title{top:72px;font-size:28px}
.field{position:absolute;height:32px;border:1px solid var(--line);display:flex;align-items:center;gap:8px;padding-left:12px;font-size:11px;color:#aaa}
.field.area{align-items:flex-start;padding-top:10px;height:82px}
.submit{left:556px;top:370px;width:88px;height:27px;background:var(--dark)}

/* footer */
.footer{top:4700px;height:390px;background:var(--footer);color:var(--white)}
.contact{position:absolute;top:96px;display:flex;align-items:center;gap:16px;font-size:11px;line-height:17px}
.contact a{color:var(--white)}
.fnav{position:absolute;top:197px;left:398px;display:flex;gap:36px;font-size:11px;text-transform:uppercase}
.fnav .active{color:var(--red)}
.badge{position:absolute;top:264px;width:76px;height:76px}
.to-top{left:1092px;top:282px;width:32px;height:32px;border-radius:50%;border:1.5px solid #999}
.bottom{top:5090px;height:34px;background:var(--footer-deep);color:#cfcfcf;font-size:11px}
.bottom .copy{position:absolute;left:98px;top:10px}
.social{position:absolute;top:8px;right:100px;display:flex;gap:14px}
.social span{width:17px;height:17px;border-radius:50%;background:#bbb}
.social .on{background:var(--red)}
</style>
</head>
<body>

<header class="hero">
  <div class="photo hero-photo" role="img" aria-label="Bright open-plan kitchen and dining room with wide oak plank floor"></div>
  <div class="abs hero-shade"></div>
  <nav class="abs nav"><span class="active">Home</span><span>About</span><span>Services</span><span>Careers</span><span>Contact Us</span></nav>
  <div class="btn btn-red cta">Free Consultation</div>
  <div class="abs brand-mark"><span class="brand-name">Norvale<br>Flooring</span></div>
  <div class="abs hero-sub">A Complete Solution for Your Flooring Vision.</div>
  <h1 class="abs hero-title">Welcome to our Norvale<br>Flooring Solutions</h1>
  <div class="abs dots"><span></span><span class="on"></span><span></span></div>
</header>

<section class="who">
  <div class="photo" role="img" aria-label="Flooring installer laying laminate planks with a toolbox beside him"></div>
  <h2 class="abs heading">Who We Are</h2>
  <p class="abs" style="top:218px">Lorem Ipsum is simply dummy text of the printing and typesetting industry. Lorem Ipsum has been the industry's standard dummy text ever since the 1500s, when an unknown printer took a galley of type and scrambled it to make a type specimen book.</p>
  <p class="abs" style="top:306px">It has survived not only five centuries, but also the leap into electronic typesetting, remaining essentially unchanged.</p>
  <div class="btn btn-dark" style="left:664px;top:368px;width:112px;height:28px">Read More</div>
</section>

<section class="where">
  <div class="photo" role="img" aria-label="Modern living and dining room with polished marble floor and patterned rug"></div>
  <div class="abs where-box">
    <h2 class="heading">Where We Work</h2>
    <p>Lorem Ipsum is simply dummy text of the printing and typesetting industry. Lorem Ipsum has been the industry's standard dummy text ever since the 1500s, when an unknown printer took a galley of type and scrambled it to make a type specimen book.</p>
    <div class="btn btn-red" style="left:32px;top:230px;width:112px;height:27px">Read More</div>
  </div>
</section>

<section class="services">
  <h2 class="heading section-title">Our Services</h2>
  <div class="card" style="left:98px;background:radial-gradient(ellipse 90px 110px at 50% 50%,rgba(150,110,75,.55),transparent 70%),linear-gradient(180deg,#e6e4df 0%,#d8d3cb 55%,#a98d72 100%)" role="img" aria-label="Hardwood floor with armchair and potted plant"><span class="card-label">Hardwood</span></div>
  <div class="card" style="left:354px;background:radial-gradient(ellipse 110px 140px at 55% 55%,rgba(150,152,148,.6),transparent 70%),linear-gradient(180deg,#5f645f,#3a3e3b)" role="img" aria-label="Natural stone slabs"><span class="card-label">Natural Stone</span></div>
  <div class="card" style="left:612px;background:radial-gradient(ellipse 120px 60px at 70% 15%,rgba(210,208,204,.7),transparent 70%),linear-gradient(180deg,#999997,#b5b4b1 60%,#a3a29f)" role="img" aria-label="Grey carpet in a living room"><span class="card-label">Carpet</span></div>
  <div class="card card-hover" style="left:868px" role="img" aria-label="Laminate floor in a bright living room">
    <span class="card-label">Laminate</span>
    <svg class="abs" style="left:20px;bottom:16px" width="26" height="26" viewBox="0 0 26 26"><circle cx="13" cy="13" r="11" fill="none" stroke="#e1262c" stroke-width="2"/><path d="M8 13h10M14 9l4 4-4 4" fill="none" stroke="#e1262c" stroke-width="2"/></svg>
  </div>
  <svg class="abs next" viewBox="0 0 36 36"><path d="M15 11l7 7-7 7" fill="none" stroke="#fff" stroke-width="2.5"/></svg>
  <div class="btn btn-dark" style="left:550px;top:524px;width:102px;height:26px">View All</div>
</section>

<section class="band" role="img" aria-label="Bedroom with white tile floor, low bed and dark rug"></section>

<section class="work">
  <h2 class="heading section-title">Work We Have Done</h2>
  <div class="tile" style="left:0;top:154px;width:400px;background:radial-gradient(ellipse 200px 60px at 50% 30%,rgba(120,120,120,.35),transparent 70%),linear-gradient(180deg,#cfd3d4,#f1f1f0 60%,#e4e4e2)" role="img" aria-label="White kitchen with glossy tile floor"></div>
  <div class="tile" style="left:400px;top:154px;width:404px;background:radial-gradient(ellipse 90px 60px at 65% 60%,rgba(245,245,245,.8),transparent 70%),linear-gradient(180deg,#b08f72 0%,#a5a39f 50%,#7d7c7a 100%)" role="img" aria-label="Bathroom with freestanding tub and grey stone tile"></div>
  <div class="tile" style="left:804px;top:154px;width:396px;background:radial-gradient(ellipse 100px 110px at 45% 45%,rgba(80,50,35,.6),transparent 70%),linear-gradient(180deg,#c9bba8,#a88d75 60%,#6f5443)" role="img" aria-label="Living room with wooden media wall"></div>
  <div class="tile" style="left:0;top:417px;width:400px;background:radial-gradient(ellipse 110px 70px at 28% 78%,rgba(215,150,80,.75),transparent 70%),linear-gradient(180deg,#5d5a58,#8d8a86 55%,#b7b4af)" role="img" aria-label="Living room with sofa and round wooden table"></div>
  <div class="tile" style="left:400px;top:417px;width:404px;background:radial-gradient(ellipse 140px 70px at 50% 80%,rgba(200,200,205,.6),transparent 70%),linear-gradient(180deg,#3a3738,#5e5a58 50%,#8e8a86)" role="img" aria-label="Lobby with polished floor and dark seating"></div>
  <div class="tile tile-note" style="left:804px;top:417px;width:396px" role="img" aria-label="Bright bathroom project">
    <span class="t">Dreamy<br>Bathroom</span><span class="s">Project</span>
    <svg class="abs" style="left:24px;top:200px" width="28" height="28" viewBox="0 0 26 26"><circle cx="13" cy="13" r="11" fill="none" stroke="#e1262c" stroke-width="2"/><path d="M8 13h10M14 9l4 4-4 4" fill="none" stroke="#e1262c" stroke-width="2"/></svg>
  </div>
  <div class="btn btn-red" style="left:550px;top:728px;width:100px;height:28px">View All</div>
</section>

<section class="insta">
  <div class="abs insta-box">
    <div class="insta-mark"><span>Norvale<br>Flooring</span></div>
    <div class="insta-text">Join us on Instagram<br>to be the first to see<br>our latest design<br>ideas and installed<br>projects</div>
    <div class="insta-handle">@norvale-floors</div>
  </div>
  <div class="collage" style="left:836px;top:44px;width:266px;height:240px;background:radial-gradient(ellipse 100px 50px at 60% 75%,rgba(90,90,95,.55),transparent 70%),linear-gradient(180deg,#8a9099,#c9ccd0 55%,#b0aea9)" role="img" aria-label="Living room with glass dining table"></div>
  <div class="collage" style="left:608px;top:82px;width:246px;height:204px;background:radial-gradient(ellipse 80px 60px at 50% 40%,rgba(230,235,225,.8),transparent 70%),linear-gradient(180deg,#cfcfca,#9a9087 70%,#7f766c)" role="img" aria-label="Dining room with large windows"></div>
  <div class="collage" style="left:584px;top:284px;width:230px;height:124px;background:radial-gradient(ellipse 60px 40px at 60% 60%,rgba(170,175,178,.6),transparent 70%),linear-gradient(180deg,#2e3032,#5e6062)" role="img" aria-label="Dark shower room with glass screen"></div>
  <div class="collage" style="left:812px;top:262px;width:274px;height:178px;background:radial-gradient(ellipse 90px 40px at 40% 78%,rgba(45,42,40,.6),transparent 70%),linear-gradient(90deg,#e8e6e1 0%,#efede9 60%,#b7a894 100%)" role="img" aria-label="Bedroom with pale floor and dark rug"></div>
</section>

<section class="consult">
  <h2 class="heading section-title">Get Free Consultation</h2>
  <div class="field" style="left:322px;top:144px;width:270px"><svg width="11" height="11" viewBox="0 0 12 12"><circle cx="6" cy="4" r="2.5" fill="none" stroke="#aaa"/><path d="M1.5 11.5c0-3 9-3 9 0" fill="none" stroke="#aaa"/></svg>Name</div>
  <div class="field" style="left:608px;top:144px;width:270px"><svg width="11" height="11" viewBox="0 0 12 12"><rect x="3" y="0.5" width="6" height="11" rx="1" fill="none" stroke="#aaa"/></svg>Phone</div>
  <div class="field" style="left:322px;top:192px;width:270px"><svg width="12" height="10" viewBox="0 0 12 10"><rect x=".5" y=".5" width="11" height="9" fill="none" stroke="#aaa"/><path d="M.5 .5l5.5 5 5.5-5" fill="none" stroke="#aaa"/></svg>Email</div>
  <div class="field" style="left:608px;top:192px;width:270px"><svg width="10" height="12" viewBox="0 0 10 12"><path d="M5 11.5S1 7 1 4.5a4 4 0 018 0C9 7 5 11.5 5 11.5z" fill="none" stroke="#aaa"/><circle cx="5" cy="4.5" r="1.3" fill="none" stroke="#aaa"/></svg>Location</div>
  <div class="field area" style="left:322px;top:240px;width:556px"><svg width="12" height="11" viewBox="0 0 12 11"><path d="M.5 .5h11v7H4l-3 3v-3H.5z" fill="none" stroke="#aaa"/></svg>How can we help?</div>
  <div class="btn submit">Submit</div>
</section>

<footer class="footer">
  <div class="contact" style="left:180px">
    <svg width="40" height="44" viewBox="0 0 40 44"><path d="M20 34S9 22 9 14a11 11 0 0122 0c0 8-11 20-11 20z" fill="none" stroke="#fff" stroke-width="2"/><circle cx="20" cy="14" r="4" fill="none" stroke="#fff" stroke-width="2"/><ellipse cx="20" cy="38" rx="16" ry="4" fill="none" stroke="#fff" stroke-width="2"/></svg>
    <div>Lorem ipsum, Suite 205<br>Harbor City, WA 98000</div>
  </div>
  <div class="contact" style="left:514px">
    <svg width="42" height="42" viewBox="0 0 42 42"><path d="M9 4l7 8-4 5c2 5 6 9 11 12l5-4 8 7-5 6C18 36 6 24 3 10z" fill="none" stroke="#fff" stroke-width="2" stroke-linejoin="round"/><path d="M25 6a11 11 0 0111 11M25 12a5 5 0 015 5" fill="none" stroke="#fff" stroke-width="2"/></svg>
    <div>(425) 555-0142 (o)<br>(425) 555-0178 (f)</div>
  </div>
  <div class="contact" style="left:816px">
    <svg width="40" height="40" viewBox="0 0 40 40"><circle cx="20" cy="20" r="17" fill="none" stroke="#fff" stroke-width="2.5"/><circle cx="20" cy="20" r="6" fill="none" stroke="#fff" stroke-width="2.5"/><path d="M26 14v9c0 4 7 4 7-3" fill="none" stroke="#fff" stroke-width="2.5"/></svg>
    <div>info@norvaleflooring.com<br><a href="#map">View Map</a></div>
  </div>
  <nav class="fnav"><span class="active">Home</span><span>About</span><span>Services</span><span>Careers</span><span>Contact Us</span></nav>
  <div class="badge" style="left:380px;background:#e7e7e7;border-radius:8px" role="img" aria-label="Service award badge"></div>
  <div class="badge" style="left:496px;background:#f4f4f4;border-radius:50%" role="img" aria-label="Expertise award badge"></div>
  <div class="badge" style="left:616px;background:#2f8a45;border-radius:50%" role="img" aria-label="Super service award badge"></div>
  <div class="badge" style="left:736px;background:#ffffff" role="img" aria-label="Best of service award badge"></div>
  <svg class="abs to-top" viewBox="0 0 32 32"><path d="M16 23V10M11 15l5-5 5 5" fill="none" stroke="#bbb" stroke-width="1.5"/></svg>
</footer>

<div class="abs bottom" style="left:0;width:1200px">
  <span class="copy">Copyright © 2023 Norvale Flooring. All Rights Reserved</span>
  <div class="social"><span></span><span class="on"></span><span></span><span></span></div>
</div>

</body>
</html>
```